Business Card Design

I am a Accounting/Bookkeeping company.  As a sideline, I am also a Notary so I would like that somewhere, either in front or perhaps the backside for the notary business.
I found a standard card I really like but didn't like the "little man" standing on the scale.
I love the colors so I am wondering if you would be able to duplicate this without the man and perhaps money or something appropriate on this side of scale
I also need help on the font.  I tend to like feminine styles but am told they are too hard to read.

Target Market(s)
Small businesses, Individuals
Industry/Entity Type
Business
Contact Information for Business Card
The Tidy Ledgerhouse
Balancing your books is our specialty
Marisol (Perkins) Dellavanti
Accounting Associate
Certified LedgerLoom TaxGuide
Notary Public
Serving Sonoma County                            707-555-3142
marisol.dellavanti@mailvexa.com

Requirements
Must have
- I would like a glossy card

```html
<!DOCTYPE html>
<html lang="en">
<head>
<meta charset="utf-8">
<title>The Tidy Ledgerhouse – Business Card</title>
<link rel="stylesheet" href="https://fonts.googleapis.com/css2?family=Della+Respira&family=Libre+Baskerville:wght@700&display=swap">
<style>
  :root {
    --card-olive: #a49c58;
    --brand-purple: #6656a6;
    --ink-brown: #4f4a36;
    --ink-soft: #5c5642;
    --scale-purple: #6f6aa8;
    --scale-orange: #e08a2a;
  }
  * { margin: 0; padding: 0; box-sizing: border-box; }
  html, body { width: 1200px; height: 702px; overflow: hidden; background: var(--card-olive); }
  .card {
    position: relative;
    width: 1200px;
    height: 702px;
    background: var(--card-olive);
    font-family: "Della Respira", Georgia, serif;
    color: var(--ink-brown);
  }
  .card > * { position: absolute; line-height: 1; white-space: nowrap; }
  .brand-name {
    left: 77px; top: 74px;
    font-size: 60px;
    color: var(--brand-purple);
    letter-spacing: 0.5px;
  }
  .tagline {
    left: 113px; top: 148px;
    font-size: 33px;
  }
  .person-name {
    left: 77px; top: 342px;
    font-size: 40px;
    font-weight: 700;
    -webkit-text-stroke: 0.6px var(--ink-brown);
  }
  .person-name .maiden { font-weight: 400; -webkit-text-stroke: 0; }
  .role-title { left: 79px; top: 408px; font-size: 35px; }
  .credential { left: 79px; top: 458px; font-size: 31px; }
  .notary { left: 79px; top: 504px; font-size: 31px; }
  .service-area {
    left: 79px; top: 622px;
    font-family: "Libre Baskerville", Georgia, serif;
    font-weight: 700;
    font-size: 29px;
    color: var(--ink-soft);
  }
  .phone {
    right: 83px; top: 570px;
    font-family: "Libre Baskerville", Georgia, serif;
    font-weight: 700;
    font-size: 37px;
    color: var(--ink-soft);
  }
  .email {
    right: 83px; top: 624px;
    font-family: "Libre Baskerville", Georgia, serif;
    font-weight: 700;
    font-size: 26px;
    color: var(--ink-soft);
  }
  .scale-art {
    left: 791px; top: 214px;
    width: 322px; height: 288px;
  }
</style>
</head>
<body>
  <main class="card">
    <h1 class="brand-name">The Tidy Ledgerhouse</h1>
    <p class="tagline">Balancing your Books is our Speciality</p>

    <p class="person-name">Marisol <span class="maiden">(Perkins)</span> Dellavanti</p>
    <p class="role-title">Accounting Specialist</p>
    <p class="credential">Certified LedgerLoom TaxGuide</p>
    <p class="notary">Notary Public</p>

    <p class="service-area">Serving Sonoma County</p>
    <p class="phone">707-555-3142</p>
    <p class="email">marisol.dellavanti@mailvexa.com</p>

    <svg class="scale-art" viewBox="0 0 322 288" role="img" aria-label="Illustration of a balance scale holding stacks of money on both pans">
      <defs>
        <linearGradient id="scale-tones" x1="0" y1="0" x2="0" y2="1">
          <stop offset="0" stop-color="var(--scale-purple)" stop-opacity="0.55"/>
          <stop offset="1" stop-color="var(--scale-orange)" stop-opacity="0.75"/>
        </linearGradient>
      </defs>
      <rect x="0" y="0" width="322" height="288" rx="24" fill="url(#scale-tones)"/>
    </svg>
  </main>
</body>
</html>
```